tovrin company need business card, envelope and letterhead design

Check on the attached file wherein you can find our logo and information about the company
Business card will double sided English version and Arabic version

Industry/Entity Type

Business

Requirements
Must have
• include the design also for the letterhead and envelop
Nice to have

```html
<!DOCTYPE html>
<html lang="en">
<head>
<meta charset="utf-8">
<title>Tovrin Business Card</title>
<link rel="stylesheet" href="https://fonts.googleapis.com/css2?family=Open+Sans:wght@400;600;700&display=swap">
<style>
  :root {
    --brand-blue: #1568bd;
    --brand-blue-dark: #0f4f93;
    --silver: #c9ced4;
    --ink: #4a4a4a;
    --paper: #ffffff;
    --backdrop: #e6e7e8;
  }
  * { margin: 0; padding: 0; box-sizing: border-box; }
  html, body { width: 1200px; height: 1021px; overflow: hidden; }
  body {
    background: var(--backdrop);
    font-family: "Open Sans", Arial, sans-serif;
    position: relative;
  }
  .card {
    position: absolute;
    left: 232px;
    width: 736px;
    height: 420px;
    box-shadow: 0 6px 18px rgba(0,0,0,0.18);
  }
  .card-front { top: 48px; background: var(--brand-blue); }
  .card-back { top: 553px; background: var(--paper); border-bottom: 6px solid var(--brand-blue); }

  .wordmark {
    position: absolute;
    display: flex;
    align-items: center;
    gap: 14px;
    font-weight: 700;
    letter-spacing: 4px;
    text-transform: uppercase;
    white-space: nowrap;
  }
  .wordmark-mark { display: block; flex: none; }
  .card-front .wordmark {
    left: 50%; top: 50%;
    transform: translate(-50%, -50%);
    color: var(--silver);
    font-size: 56px;
  }
  .card-front .wordmark-mark { width: 50px; height: 50px; background: var(--silver); }
  .card-back .wordmark {
    right: 56px; top: 62px;
    color: var(--brand-blue);
    font-size: 34px;
  }
  .card-back .wordmark-mark { width: 32px; height: 32px; background: var(--brand-blue); }

  .holder {
    position: absolute;
    left: 52px; top: 150px;
    padding-left: 14px;
    border-left: 9px solid var(--brand-blue);
  }
  .holder-name { font-size: 24px; color: var(--ink); line-height: 1.15; white-space: nowrap; }
  .holder-role { font-size: 17px; color: var(--brand-blue); line-height: 1.25; white-space: nowrap; }

  .contact-list {
    position: absolute;
    left: 56px; top: 262px;
    list-style: none;
    font-size: 15px;
    color: var(--ink);
    line-height: 1.3;
  }
  .contact-list li { display: flex; align-items: flex-start; gap: 10px; margin-bottom: 4px; white-space: nowrap; }
  .contact-icon { width: 14px; height: 14px; flex: none; margin-top: 3px; fill: var(--brand-blue); }
</style>
</head>
<body>
  <section class="card card-front" aria-label="Card front">
    <div class="wordmark"><span class="wordmark-mark"></span>Tovrin</div>
  </section>

  <section class="card card-back" aria-label="Card back">
    <div class="wordmark"><span class="wordmark-mark"></span>Tovrin</div>

    <div class="holder">
      <p class="holder-name">Faris Bin Omar Al Rashidi</p>
      <p class="holder-role">General Manager/ +966 555 310 482</p>
    </div>

    <ul class="contact-list">
      <li>
        <svg class="contact-icon" viewBox="0 0 14 14"><path d="M7 0a5 5 0 0 0-5 5c0 3.6 5 9 5 9s5-5.4 5-9a5 5 0 0 0-5-5zm0 7a2 2 0 1 1 0-4 2 2 0 0 1 0 4z"/></svg>
        <span>Khalid Bin Waleed Road- Al Nakheel-<br>P.O. Box 4152-11834</span>
      </li>
      <li>
        <svg class="contact-icon" viewBox="0 0 14 14"><path d="M1 4c0-1.5 2.5-3 6-3s6 1.5 6 3v1H10V4H4v1H1zM3 6h8l1 7H2z"/></svg>
        <span>011 4720633</span>
      </li>
      <li>
        <svg class="contact-icon" viewBox="0 0 14 14"><rect x="3" y="1" width="8" height="4"/><rect x="1" y="5" width="12" height="6" rx="1"/><rect x="3" y="9" width="8" height="4"/></svg>
        <span>011 4720 744</span>
      </li>
      <li>
        <svg class="contact-icon" viewBox="0 0 14 14"><path d="M1 3h12v1L7 8 1 4zM1 5.5l6 4 6-4V11H1z"/></svg>
        <span>tovrin.sa@mailbox.com</span>
      </li>
    </ul>
  </section>
</body>
</html>
```